Speisekarten-Design für mediterranes Restaurant
Zielgruppe
Wir eröffnen am 23.09.2022 ein Restaurant im Hotel SolBrunn Bad Farnhain in 94999 Fürstenzell unter dem Namen 'VELO'. Die Übersetzung aus dem Portugiesischem bedeutet 'Seele' - Velo soll also die Seele des Hauses werden und unsere Gäste aus nah&fern und ob jung oder alt mit mediterranen, besonderen Köstlichkeiten unseres Küchenchefs Matteo Carvalhal verwöhnen.
Auf der Speisekarte stehen Bruch & Frühstück (z.B. Joghurt mit Früchten und Agavensirup, Pancakes und Waffeln, Egg Benedikt aber auch bayerische Spezialitäten wie Weißwurst mit Breze). Weiterhin werden wir Tapas (vegatarisch, Fleisch, Fisch) anbieten. Als USP steht die original portugiesische Cataplana oder Hähnchen nach Art des Hauses auf der Karte. Hinzu kommen noch Desserts. Ebenso benötigen wir eine Wochenkarte sowie eine Getränkekarte (Softdrinks, Kaffee, Tee, Bier, Wein, Long Drinks, etc.) Ich denke eine Seite sollte für Frühstück/Brunch und eine für Vorspeisen, Tapas, Hauptspeisen vorgesehen werden und ein Blatt für die Wochenkarte. Weiterhin ein Blatt mit normalen Getränken und eine Weinkarte.
Wir suchen ein modernes, zeitloses Design für unsere neue Speisekarte. Diese soll auf einzelnen Blättern in einem Klemmbrett aus Holz eingespannt werden. Wichtig ist uns, dass wir die Gerichte und Getränke jederzeit in einem festen Design ändern und selbst drucken können.
Die hochgeladenen Speisekarten im Word-Format dienen nur der Orientierung für Anzahl, etc. Die Karten müssen selbstständig durch uns ergänzt oder geändert werden können. Anbei auch ein Beispielbild, welches über entwurfmarkt.de in Bildwand gefunden wurde.
Aufgabenstellung
als DIN-Format wählen wir A4.
Gerichte wir die Cataplana sollten eine Erklärung beinhalten, die auch noch gut aussieht und nicht nur in Klammern unter dem Gericht steht.

```html
<!DOCTYPE html>
<html lang="de">
<head>
<meta charset="utf-8">
<title>VELO – Speisekarten</title>
<link rel="stylesheet" href="https://fonts.googleapis.com/css2?family=Fira+Sans+Condensed:wght@300;400;600;700&family=Fira+Sans+Extra+Condensed:wght@700;800&display=swap">
<style>
  :root{
    --paper:#ffffff;
    --ink:#1d1d1d;
    --ink-soft:#555555;
    --line:#2a2a2a;
    --backdrop:#e9e7e3;
    --shade:#cfcfcf;
  }
  *{box-sizing:border-box;margin:0;padding:0}
  html,body{width:1200px;height:848px;overflow:hidden}
  body{background:var(--backdrop);font-family:"Fira Sans Condensed",sans-serif;color:var(--ink);position:relative}
  .page{position:absolute;top:28px;width:560px;height:792px;background:var(--paper);box-shadow:0 2px 8px rgba(0,0,0,.12)}
  .page--brunch{left:30px}
  .page--tapas{left:610px}
  .frame{position:absolute;inset:0;width:560px;height:792px}
  .frame path,.frame rect{fill:none;stroke:var(--line);stroke-width:1.6}
  .title{position:absolute;top:20px;left:0;right:0;text-align:center}
  .title h1{display:inline-block;background:var(--paper);padding:0 10px;font-family:"Fira Sans Extra Condensed",sans-serif;font-weight:800;font-size:30px;line-height:1;letter-spacing:.2px}
  .title p{font-weight:300;font-size:14px;margin-top:2px}
  .brand{position:absolute;top:58px;right:30px;display:flex;align-items:center;gap:6px}
  .brand span{font-family:"Fira Sans Condensed",sans-serif;font-weight:400;font-size:24px;letter-spacing:2px}
  .brand i{display:block;width:10px;height:10px;border:1.4px solid var(--ink);border-radius:50%}
  .block{position:absolute}
  .item{margin-bottom:10px}
  .item-head{display:flex;justify-content:space-between;align-items:baseline;gap:6px}
  .name{font-weight:700;font-size:12.5px;line-height:1.15}
  .price{font-weight:600;font-size:12px;white-space:nowrap}
  .desc{font-weight:300;font-size:9.5px;line-height:1.25;color:var(--ink-soft)}
  .extra{display:flex;justify-content:space-between;font-weight:300;font-size:9.5px;line-height:1.25;color:var(--ink-soft)}
  .boxed{border:1.4px solid var(--line);border-radius:10px;padding:8px 10px}
  .list-row{display:flex;justify-content:space-between;font-size:10.5px;line-height:1.45}
  .list-row b{font-weight:600}
  .section-head{position:absolute;display:flex;align-items:center;gap:10px}
  .section-head h2{font-family:"Fira Sans Extra Condensed",sans-serif;font-weight:800;font-size:22px;letter-spacing:.3px}
  .leaf{display:block;width:24px;height:14px;background:var(--shade);border-radius:50%}
  .rule{position:absolute;height:0;border-top:1.4px solid var(--line)}
  .vrule{position:absolute;width:0;border-left:1.4px solid var(--line)}
  .eggs{text-align:center}
  .eggs .sun{width:80px;height:26px;margin:0 auto 4px;border-radius:40px 40px 0 0;background:linear-gradient(#e2e2e2,#f3f3f3)}
  .eggs strong{display:block;font-family:"Fira Sans Extra Condensed",sans-serif;font-weight:800;font-size:32px;line-height:1}
  .eggs em{display:block;font-style:normal;font-weight:300;font-size:15px;line-height:1.1}
  .duo h3{font-family:"Fira Sans Extra Condensed",sans-serif;font-weight:800;font-size:17px;text-align:center;margin-bottom:6px}
  .duo ul{list-style:none;font-size:10px;font-weight:300;line-height:1.45;text-align:center}
  .duo .duo-price{font-size:10px;font-weight:600;text-align:center;margin-top:8px}
  .big-head{font-family:"Fira Sans Extra Condensed",sans-serif;font-weight:800;font-size:38px;line-height:.95;text-align:center}
  .croissant{width:24px;height:12px;background:var(--shade);border-radius:12px 12px 4px 4px;margin:6px auto 0}
</style>
</head>
<body>

<!-- Frühstück & Brunch -->
<section class="page page--brunch">
  <svg class="frame" viewBox="0 0 560 792" aria-hidden="true"><rect x="18" y="36" width="524" height="736" rx="14"/></svg>
  <header class="title"><h1>Frühstück &amp; Brunch</h1><p>Von 8.00 bis 13.00 Uhr</p></header>
  <div class="brand"><i></i><span>VELO</span></div>

  <div class="block" style="left:36px;top:88px;width:162px">
    <div class="item"><div class="item-head"><span class="name">Süßer Beginn</span><span class="price">5,50</span></div>
      <p class="desc">Croissant, Butter, Marmelade, Honig und frischer Obstsalat</p></div>
    <div class="item"><div class="item-head"><span class="name">Fresh Fruit Joghurt<br>&amp; Agavensirup</span><span class="price">5,50</span></div>
      <p class="desc">mit frischen Früchten der Saison</p>
      <p class="extra"><span>mit Granola</span><span>+ 1,00</span></p>
      <p class="extra"><span>mit Nüssen</span><span>+ 1,00</span></p></div>
    <div class="item"><div class="item-head"><span class="name">Eier im Glas</span><span class="price">5,50</span></div>
      <p class="desc">2 pochierte Eier mit Kräutern, Schnittlauch und Brot</p></div>
    <div class="item"><div class="item-head"><span class="name">Egg Benedict</span><span class="price">9,50</span></div>
      <p class="desc">English Muffin mit pochierten Eiern, Schinken und Sauce Hollandaise</p>
      <p class="extra"><span>mit Lachs</span><span>+ 1,00</span></p>
      <p class="extra"><span>mit Avocado</span><span>+ 1,50</span></p></div>
  </div>

  <div class="block boxed" style="left:214px;top:104px;width:130px">
    <p class="list-row"><b>Gemischtes Brot</b><span>2,50</span></p>
    <p class="list-row"><span>Breze</span><span>1,50</span></p>
    <p class="list-row"><span>Croissant</span><span>2,00</span></p>
    <p class="list-row"><span>Franzbrötchen</span><span>2,00</span></p>
    <p class="list-row"><span>Pain au Chocolat</span><span>2,00</span></p>
    <p class="list-row"><span>Quiche</span><span>4,00</span></p>
    <p class="list-row"><span>Kuchen</span><span>3,50</span></p>
  </div>
  <div class="block" style="left:264px;top:250px;width:30px"><div class="croissant" role="img" aria-label="Kleines Croissant-Symbol"></div></div>

  <div class="block eggs" style="left:205px;top:280px;width:150px">
    <div class="sun" role="img" aria-label="Aufgehende Sonne als Zeichnung"></div>
    <strong>BIO-EIER</strong>
    <em>von glücklichen<br>Hühnern</em>
  </div>

  <div class="block" style="left:362px;top:100px;width:164px">
    <div class="item"><div class="item-head"><span class="name">Bircher Müsli</span><span class="price">6,50</span></div>
      <p class="desc">mit Haferflocken, Äpfeln, Nüssen und frischen Beeren</p></div>
    <div class="item" style="margin-top:18px"><div class="item-head"><span class="name">Pancakes &amp; Waffeln</span><span class="price">8,50</span></div>
      <p class="desc">mit Puderzucker und Ahornsirup</p>
      <p class="extra"><span>mit Früchten</span><span>+ 1,00</span></p>
      <p class="extra"><span>mit Speck</span><span>+ 2,00</span></p>
      <p class="extra"><span>mit Eis</span><span>+ 2,00</span></p></div>
    <div class="item" style="margin-top:20px"><div class="item-head"><span class="name">Rührei / Spiegeleier</span><span class="price">5,00</span></div>
      <p class="desc">mit Brot und Butter</p>
      <p class="extra"><span>mit Speck</span><span>+ 1,00</span></p>
      <p class="extra"><span>mit Käse</span><span>+ 1,50</span></p></div>
    <div class="item"><div class="item-head"><span class="name">Egg Royale</span><span class="price">9,50</span></div>
      <p class="desc">English Muffin mit pochierten Eiern, Lachs, Avocado und Sauce Hollandaise</p>
      <p class="extra"><span>mit Spinat</span><span>+ 1,50</span></p>
      <p class="extra"><span>mit Tomate</span><span>+ 2,00</span></p></div>
  </div>

  <div class="section-head" style="left:40px;top:398px"><span class="leaf" role="img" aria-label="Blatt-Ornament"></span><h2>EINFACH WEIL ES GUT IST</h2></div>
  <div class="rule" style="left:36px;right:36px;top:432px"></div>

  <div class="block" style="left:36px;top:442px;width:92px">
    <div class="item"><div class="item-head"><span class="name">WURSTBRETT</span></div>
      <p class="desc">Salami, Schinken &amp; Kräuterbutter</p><p class="price">7,50</p></div>
  </div>
  <div class="block" style="left:140px;top:442px;width:88px">
    <div class="item"><div class="item-head"><span class="name">KÄSEBRETT</span></div>
      <p class="desc">Käse, Butter &amp; Breze</p><p class="price">7,50</p></div>
  </div>
  <div class="block" style="left:238px;top:442px;width:100px">
    <div class="item"><div class="item-head"><span class="name">LACHSTELLER</span></div>
      <p class="desc">mit Meerrettich und Brot</p><p class="price">8,50</p></div>
  </div>
  <div class="vrule" style="left:342px;top:440px;height:70px"></div>
  <div class="block" style="left:350px;top:448px;width:176px">
    <div class="item"><div class="item-head"><span class="name">FRÜHSCHOPPEN</span></div>
      <p class="desc">2 Weißwürste mit Breze, süßem Senf und einem Bier</p><p class="price">5,50</p></div>
  </div>

  <div class="block" style="left:36px;top:520px;width:146px">
    <div class="item"><div class="item-head"><span class="name">AVOCADO STULLE</span><span class="price">6,50</span></div>
      <p class="desc">Sauerteigbrot mit Avocado, Salat und Tomate</p>
      <p class="extra"><span>mit Lachs</span><span>+ 2,00</span></p>
      <p class="extra"><span>mit Speck</span><span>+ 2,50</span></p>
      <p class="extra"><span>mit Ei</span><span>+ 2,00</span></p></div>
  </div>

  <div class="block boxed duo" style="left:192px;top:520px;width:170px;height:226px">
    <h3>FRÜHSTÜCK DUO</h3>
    <ul>
      <li>Brotkorb</li>
      <li>+ 2 Croissants + Butter</li>
      <li>+ Wurst- &amp; Käsebrett</li>
      <li>+ Rührei</li>
      <li>+ Pancakes „all in one“</li>
      <li>+ Obstsalat</li>
      <li>+ Marmelade, Honig &amp; Nussina</li>
      <li>+ 2 O-Saft frisch gepresst</li>
      <li>+ 2 Heißgetränke</li>
    </ul>
    <p class="duo-price">45,00 für 2 Pers.</p>
  </div>

  <div class="block" style="left:376px;top:528px;width:150px">
    <div class="item"><div class="item-head"><span class="name">SHAKSHUKA</span><span class="price">8,50</span></div>
      <p class="desc">pochierte Eier in würziger Tomatensauce mit Paprika, Feta und Brot</p></div>
  </div>
</section>

<!-- Tapas & Brotzeit -->
<section class="page page--tapas">
  <svg class="frame" viewBox="0 0 560 792" aria-hidden="true"><path d="M32,36 H528 A14,14 0 0 0 542,50 V758 A14,14 0 0 0 528,772 H32 A14,14 0 0 0 18,758 V50 A14,14 0 0 0 32,36 Z"/></svg>
  <header class="title"><h1>Tapas &amp; Brotzeit</h1><p>Von 16.00 bis 22.00 Uhr</p></header>
  <div class="brand"><i></i><span>VELO</span></div>

  <div class="block" style="left:36px;top:92px;width:150px">
    <div class="item"><div class="item-head"><span class="name">Tapassuppe</span><span class="price">5,50</span></div>
      <div class="item-head"><span class="name">Gewürzte Oliven</span><span class="price">2,50</span></div></div>
    <div class="item"><div class="item-head"><span class="name">Kroketten</span><span class="price">2,50</span></div>
      <p class="desc">mit Schinken oder Käse und Aioli</p></div>
    <div class="item"><div class="item-head"><span class="name">Papas Arrugadas</span><span class="price">4,00</span></div>
      <p class="desc">kanarische Salzkartoffeln</p></div>
    <div class="item"><div class="item-head"><span class="name">Obazda</span><span class="price">4,50</span></div>
      <p class="desc">mit Breze, Radieserl und Zwiebeln</p></div>
    <div class="item"><div class="item-head"><span class="name">Bruschetta</span><span class="price">6,50</span></div>
      <p class="desc">Pico-de-Gallo mit Knoblauchbrot, Tomaten und Basilikum</p></div>
  </div>

  <div class="block" style="left:202px;top:92px;width:154px">
    <div class="item"><div class="item-head"><span class="name">Gemischter Brotkorb</span><span class="price">2,50</span></div></div>
    <div class="boxed" style="margin-top:2px">
      <p class="list-row"><span>Pesto Rosso</span><span>1,50</span></p>
      <p class="list-row"><span>Tomatenpesto</span><span>1,50</span></p>
      <p class="list-row"><span>Chimichurri</span><span>1,50</span></p>
      <p class="list-row"><span>Aioli</span><span>1,50</span></p>
      <p class="list-row"><span>Pico de Gallo</span><span>1,50</span></p>
      <p class="list-row"><span>Olivetapenade</span><span>1,50</span></p>
      <p class="list-row"><span>Hummus</span><span>1,50</span></p>
    </div>
    <div class="item" style="margin-top:16px"><div class="item-head"><span class="name">Pimientos del Piquillo</span><span class="price">3,50</span></div>
      <p class="desc">eingelegte Paprikaschoten</p></div>
    <div class="item"><div class="item-head"><span class="name">Pimientos de Padrón</span><span class="price">4,50</span></div>
      <p class="desc">gebratene grüne Paprika</p></div>
  </div>

  <div class="block" style="left:372px;top:92px;width:154px">
    <div class="item"><div class="item-head"><span class="name">Karotten</span><span class="price">2,00</span></div>
      <p class="desc">mit Kreuzkümmel, Kräutern und Essig</p></div>
    <div class="item"><div class="item-head"><span class="name">Antipasti-Spieße</span><span class="price">5,00</span></div>
      <p class="desc">Zucchini, Aubergine, Paprika und Mozzarella</p></div>
    <div class="item"><div class="item-head"><span class="name">Ziegenkäse</span><span class="price">6,50</span></div>
      <p class="desc">gratiniert mit Honig und Walnüssen</p></div>
    <div class="item"><div class="item-head"><span class="name">Büffelmozzarella</span><span class="price">10,50</span></div>
      <p class="desc">mit Tomaten, Rucola und Balsamico-Creme</p></div>
    <div class="item"><div class="item-head"><span class="name">Huevos Rancheros</span><span class="price">9,00</span></div>
      <p class="desc">Spiegeleier auf Tortilla mit Bohnen, Salsa und Pico de Gallo</p></div>
  </div>

  <div class="rule" style="left:36px;width:150px;top:420px"></div>
  <div class="rule" style="left:372px;width:154px;top:420px"></div>

  <div class="block" style="left:36px;top:434px;width:150px">
    <div class="item"><div class="item-head"><span class="name">Pflaumen</span><span class="price">4,00</span></div>
      <p class="desc">im Speckmantel</p></div>
    <div class="item"><div class="item-head"><span class="name">Cassoulet</span><span class="price">7,50</span></div>
      <p class="desc">Bohneneintopf mit zartem Fleisch und würziger Chorizo</p></div>
    <div class="item" style="margin-top:22px"><div class="item-head"><span class="name">Knusprige Garnelen</span><span class="price">7,50</span></div>
      <p class="desc">im Panko-Mantel mit hausgemachter Aioli</p></div>
  </div>

  <div class="block" style="left:202px;top:430px;width:154px;text-align:center">
    <span class="leaf" role="img" aria-label="Blatt-Ornament" style="margin:0 auto 10px"></span>
    <div class="item" style="text-align:left"><div class="item-head"><span class="name">Wurst &amp; Käsebrett</span><span class="price">7,50</span></div>
      <p class="desc">Schinken, Salami, Edamer, Brie und Obazda</p></div>
    <div class="big-head" style="margin-top:26px">FLEISCH<br>&amp; FISCH</div>
    <div class="item" style="text-align:left;margin-top:26px"><div class="item-head"><span class="name">Boquerones en Vinagre</span><span class="price">6,00</span></div>
      <p class="desc">in Olivenöl und Weinessig eingelegte Sardellenfilets mit Knoblauch</p></div>
  </div>

  <div class="block" style="left:372px;top:430px;width:154px">
    <span class="leaf" role="img" aria-label="Blatt-Ornament" style="margin:0 auto 10px"></span>
    <div class="item"><div class="item-head"><span class="name">Albóndigas</span><span class="price">5,50</span></div>
      <p class="desc">Hackbällchen in Tomatensauce</p></div>
    <div class="item"><div class="item-head"><span class="name">Chorizo</span><span class="price">5,50</span></div>
      <p class="desc">gegrillte spanische Paprikawurst</p></div>
    <div class="item" style="margin-top:24px"><div class="item-head"><span class="name">Gambas Pil Pil</span><span class="price">7,50</span></div>
      <p class="desc">Garnelen mit Chili und Knoblauch</p></div>
  </div>
</section>

</body>
</html>
```